Stainless Steel Water Bottle Packaging

We need a design for our cylindrical water bottle packaging.

Please see attached template (500ml cola bottle template .ai file) for exact dimensions.

VORO is defined as the elemental forces of nature embodied in an object or person. The design should be eye catching and draw potential clients in. Although its a cylindrical bottle/box, the front which would face the customer when sitting on a shelf should clearly display our logo.

Industry/Entity Type

Steel

Requirements
Must have
• Designed to the specifications of the attached template (see attached)
• Our VORO Logo (see attached) and website www.vorobottle.example(in smaller font) must appear.
• Size of bottle must appear - '17 oz/500 ml'
• These should appear somewhere:
• 'INULATED DOUBLE-WALL STAINLESS STEEL WATER BOTTLE'
• 'VORO Bottles magically keeps drinks cold for up to 24hrs, hot for 12',
• 'BPA Free'
• 'For every VORO bottle purchased, a portion of proceeds will go towards charity. Each of our colour's have been assigned a specific charity. Please visit www.vorobottle.example to find out which charity you helped support!'
• The Top circle - just our Symbol (flame/drop)
• The bottom circle - 'Inc. Designed in Canada made in China' on the outer edge leaving the middle empty for the UPC code.
• Reference website for the bottle case I'm looking for:
• http://shopkorinday.example/t-flow-lagoon-pink-insulated-water-bottle
Nice to have
• illustration of our water bottle shape (see attached) appearing somewhere on the box is something i had in mind but definitely not necessary.

```html
<!DOCTYPE html>
<html lang="en">
<head>
<meta charset="utf-8">
<title>VORO Bottle Packaging Dieline</title>
<link rel="stylesheet" href="https://fonts.googleapis.com/css2?family=Open+Sans:wght@400;600;700;800&display=swap">
<style>
  :root {
    --stage: #888888;
    --navy: #082b3d;
    --sky: #35a7d8;
    --sun: #f4c322;
    --white: #ffffff;
    --guide: #c0272d;
    --leaf: #3cb93a;
  }
  * { margin: 0; padding: 0; box-sizing: border-box; }
  html, body { width: 1200px; height: 1200px; overflow: hidden; }
  body {
    background: var(--stage);
    font-family: "Open Sans", sans-serif;
    color: var(--white);
    position: relative;
  }
  .wrap-panel {
    position: absolute;
    left: 21px; top: 150px;
    width: 799px; height: 902px;
    background: var(--navy);
    border: 1px solid var(--guide);
    overflow: hidden;
  }
  .guide { position: absolute; background: var(--guide); }
  .guide--v { width: 1px; top: 0; bottom: 0; left: 30px; }
  .guide--h { height: 1px; left: 30px; right: 0; }
  .guide--top { top: 31px; }
  .guide--header { top: 198px; }
  .guide--bottom { top: 870px; }

  .brand {
    position: absolute; left: 0; right: 0; top: 76px;
    display: flex; align-items: center; justify-content: center; gap: 16px;
    padding-left: 20px;
  }
  .brand__dot { width: 34px; height: 34px; border-radius: 50%; background: var(--sun); }
  .brand__name {
    font-weight: 600; font-size: 74px; line-height: 1;
    color: var(--sky); letter-spacing: 6px;
  }
  .brand__url {
    position: absolute; left: 20px; right: 0; top: 148px;
    text-align: center; font-weight: 700; font-size: 16px;
  }

  .side-band {
    position: absolute; left: 236px; top: 199px;
    width: 58px; height: 703px;
    background: var(--sky);
  }
  .side-band__text {
    position: absolute; left: 50%; top: 336px;
    transform: translate(-50%, -50%) rotate(-90deg);
    white-space: nowrap; font-weight: 600; font-size: 20.5px;
  }

  .bottle-art {
    position: absolute; left: 322px; top: 210px;
    width: 152px; height: 568px;
    border-radius: 40px 40px 24px 24px;
    background: linear-gradient(160deg, var(--sky) 0%, var(--sky) 30%, var(--sun) 32%, var(--sun) 66%, var(--sky) 68%, var(--sky) 100%);
  }
  .size-block {
    position: absolute; left: 300px; width: 196px; top: 792px; text-align: center;
  }
  .size-block__name { font-weight: 600; font-size: 22px; color: var(--sky); letter-spacing: 2px; line-height: 1; }
  .size-block__vol { font-weight: 700; font-size: 14px; margin-top: 6px; }

  .claim {
    position: absolute; left: 622px; width: 145px; top: 304px;
    font-weight: 600; font-size: 17px; line-height: 21.6px; text-align: center;
  }
  .claim__line--split { display: flex; justify-content: space-between; }
  .claim__magic { color: var(--sky); letter-spacing: 4.5px; }

  .charity {
    position: absolute; left: 614px; top: 467px;
    width: 156px; height: 165px;
    border: 2px solid var(--sky);
    padding: 20px 15px 0 17px;
    font-size: 8.4px; line-height: 9.2px; font-weight: 400;
    text-align: justify; text-transform: uppercase;
  }
  .charity p + p { margin-top: 10px; }
  .charity .accent { color: var(--sky); }

  .bpa-badge {
    position: absolute; left: 664px; top: 697px;
    width: 56px; height: 56px; border-radius: 50%;
    background: var(--leaf); border: 3px solid var(--white);
    display: flex; flex-direction: column; align-items: center; justify-content: center;
    font-weight: 800; font-size: 12px; line-height: 11px; text-align: center;
  }

  .lid { position: absolute; left: 877px; width: 262px; height: 262px; border-radius: 50%; background: var(--navy); }
  .lid--top { top: 187px; display: flex; align-items: center; justify-content: center; }
  .lid--top .lid__name { font-weight: 600; font-size: 44px; color: var(--sky); letter-spacing: 3px; }
  .lid--bottom { top: 523px; }
  .lid--bottom svg { display: block; }
</style>
</head>
<body>
  <section class="wrap-panel" aria-label="Bottle wrap">
    <div class="guide guide--v"></div>
    <div class="guide guide--h guide--top"></div>
    <div class="guide guide--h guide--header"></div>
    <div class="guide guide--h guide--bottom"></div>

    <div class="brand">
      <span class="brand__dot"></span>
      <span class="brand__name">VORO</span>
    </div>
    <div class="brand__url">www.vorobottle.example</div>

    <div class="side-band">
      <div class="side-band__text">INULATED DOUBLE-WALL STAINLESS STEEL WATER BOTTLE</div>
    </div>

    <div class="bottle-art" role="img" aria-label="Illustration of the water bottle with a blue and yellow diagonal stripe"></div>

    <div class="size-block">
      <div class="size-block__name">VORO</div>
      <div class="size-block__vol">17 OZ/500 ML</div>
    </div>

    <div class="claim">
      <div class="claim__line--split"><span>VORO</span><span>BOTTLES</span></div>
      <div class="claim__magic">MAGICALLY</div>
      <div class="claim__line--split"><span>KEEPS</span><span>DRINKS</span></div>
      <div>COLD FOR</div>
      <div>UP TO 24HRS,</div>
      <div>HOT FOR 12</div>
    </div>

    <div class="charity">
      <p>For every <span class="accent">VORO</span> bottle purchased, a portion of proceeds will go towards charity. Each of our colour's have been assigned a specific charity.</p>
      <p>Please visit <span class="accent">www.vorobottle.example</span> to find out which charity you helped support!</p>
    </div>

    <div class="bpa-badge"><span>BPA</span><span>FREE</span></div>
  </section>

  <div class="lid lid--top" aria-label="Top circle">
    <span class="lid__name">VORO</span>
  </div>

  <div class="lid lid--bottom" aria-label="Bottom circle">
    <svg width="262" height="262" viewBox="0 0 262 262">
      <defs>
        <path id="rim-arc" d="M 131 131 m -108 0 a 108 108 0 1 1 216 0 a 108 108 0 1 1 -216 0"/>
      </defs>
      <circle cx="131" cy="131" r="120" fill="none" stroke="#ffffff" stroke-width="2"/>
      <text font-family="Open Sans, sans-serif" font-size="9" font-weight="600" fill="#ffffff" text-anchor="middle">
        <textPath href="#rim-arc" startOffset="25%">INC. DESIGNED IN CANADA MADE IN CHINA</textPath>
      </text>
    </svg>
  </div>
</body>
</html>
```